Letterhead to Introduce a 'Sister' Company.

What I am needing is a design for a letter head to introduce our current customers base of (KT Alarm) customers to our new service, 'Kestrel Tide Solar Brokers'

```html
<!DOCTYPE html>
<html lang="en">
<head>
<meta charset="utf-8">
<title>Kestrel Tide Solar Brokers — Letterhead</title>
<link href="https://fonts.googleapis.com/css2?family=Lato:wght@400;700&family=Great+Vibes&display=swap" rel="stylesheet">
<style>
  :root {
    --navy: #1b3a6b;
    --orange: #f5a01f;
    --ink: #4a4a4a;
    --ink-dark: #333333;
    --backdrop: #eceef0;
    --paper: #ffffff;
    --contact: #ffffff;
  }
  * { box-sizing: border-box; margin: 0; padding: 0; }
  html, body { width: 1200px; height: 1200px; overflow: hidden; }
  body {
    background: var(--backdrop);
    font-family: "Lato", Arial, sans-serif;
    color: var(--ink);
    position: relative;
  }
  .letterhead {
    position: absolute;
    left: 195px; top: 40px;
    width: 810px; height: 1120px;
    background: var(--paper);
    box-shadow: 0 6px 24px rgba(0,0,0,0.12);
    overflow: hidden;
  }
  .contact-band {
    position: absolute;
    right: 0; top: 14px;
    width: 440px; height: 172px;
    background: var(--navy);
    padding: 26px 28px 0 0;
    text-align: right;
    color: var(--contact);
    font-size: 13px;
    line-height: 1.55;
  }
  .contact-band::after {
    content: "";
    position: absolute;
    left: -8px; bottom: -7px;
    width: 150px; height: 7px;
    background: var(--orange);
  }
  .contact-line { display: flex; justify-content: flex-end; align-items: center; gap: 8px; }
  .contact-line .label { color: var(--orange); }
  .contact-icon { width: 13px; height: 13px; flex: none; }
  .contact-spacer { width: 13px; flex: none; }

  .brand {
    position: absolute;
    left: 60px; top: 150px;
    width: 300px;
  }
  .brand-name {
    display: flex; align-items: center; gap: 10px;
    color: var(--navy);
    font-weight: 700;
    font-size: 22px;
    line-height: 1.1;
    letter-spacing: 0.5px;
    text-transform: uppercase;
  }
  .brand-dot { width: 20px; height: 20px; border-radius: 50%; background: var(--orange); flex: none; }
  .brand-rule { margin-top: 10px; height: 2px; background: var(--orange); width: 270px; }

  .letter {
    position: absolute;
    left: 60px; top: 300px;
    width: 640px;
  }
  .date { font-size: 15px; color: var(--ink); margin-bottom: 20px; }
  .recipient-name { color: var(--orange); font-size: 17px; letter-spacing: 0.3px; }
  .recipient-role { font-size: 15px; margin-bottom: 22px; }
  .recipient-address { font-size: 15px; line-height: 1.35; margin-bottom: 22px; }
  .salutation { font-weight: 700; color: var(--ink-dark); font-size: 15px; margin-bottom: 22px; }
  .body-copy { padding-left: 62px; font-size: 13px; line-height: 1.5; color: var(--ink); }
  .body-copy p { margin-bottom: 20px; }
  .closing { display: flex; align-items: flex-end; gap: 40px; padding-left: 62px; margin-top: 30px; }
  .closing-word { font-size: 15px; }
  .signature {
    font-family: "Great Vibes", cursive;
    font-size: 52px;
    color: #111;
    line-height: 1;
  }
</style>
</head>
<body>
  <main class="letterhead">
    <header class="contact-band">
      <div class="contact-line">2840 Harbor View Lane<span class="contact-spacer"></span></div>
      <div class="contact-line">Dalton, GA 30720<span class="contact-spacer"></span></div>
      <div class="contact-line">555.201.4836
        <svg class="contact-icon" viewBox="0 0 16 16"><path fill="#f5a01f" d="M3 1h3l1.5 4-2 1.2a9 9 0 0 0 4.3 4.3L11 8.5l4 1.5v3a2 2 0 0 1-2 2C7 15 1 9 1 3a2 2 0 0 1 2-2z"/></svg>
      </div>
      <div class="contact-line"><span><span class="label">(Fax)</span>555.201.4836</span>
        <svg class="contact-icon" viewBox="0 0 16 16"><rect x="2" y="6" width="12" height="7" rx="1" fill="#f5a01f"/><rect x="4" y="2" width="8" height="4" fill="#f5a01f"/></svg>
      </div>
      <div class="contact-line">kestreltide@mailbox.com
        <svg class="contact-icon" viewBox="0 0 16 16"><rect x="1" y="3" width="14" height="10" rx="1" fill="#f5a01f"/><path d="M1.5 4 8 9l6.5-5" stroke="#1b3a6b" stroke-width="1.3" fill="none"/></svg>
      </div>
      <div class="contact-line">www.kestreltidesolar.com
        <svg class="contact-icon" viewBox="0 0 16 16"><circle cx="8" cy="8" r="6.5" fill="#f5a01f"/><path d="M1.5 8h13M8 1.5c-3 3-3 10 0 13M8 1.5c3 3 3 10 0 13" stroke="#1b3a6b" stroke-width="1" fill="none"/></svg>
      </div>
    </header>

    <div class="brand">
      <div class="brand-name"><span class="brand-dot"></span><span>Kestrel Tide Solar Brokers</span></div>
      <div class="brand-rule"></div>
    </div>

    <section class="letter">
      <p class="date">September 21-2020</p>
      <p class="recipient-name">MR. DANIEL ROURKE</p>
      <p class="recipient-role">President</p>
      <p class="recipient-address">2840 Harbor View Lane<br>Dalton, GA 30720</p>
      <p class="salutation">Dear Mr. Daniel</p>
      <div class="body-copy">
        <p>This is Photoshop's version of Lorem Ipsum. Proin gravida nibh vel velit auctor aliquet. Aenean sollicitudin, lorem quis bibendum auctor, nisi elit consequat ipsum, nec sagittis sem nibh id elit. Duis sed odio sit amet nibh vulputate cursus a sit amet mauris. Morbi accumsan ipsum velit. Nam nec tellus a odio tincidunt auctor a ornare odio. Sed non mauris elit.</p>
        <p>This is Photoshop's version of Lorem Ipsum. Proin gravida nibh vel velit auctor aliquet. Aenean sollicitudin, lorem quis bibendum auctor, nisi elit consequat ipsum, nec sagittis sem nibh id elit. Duis sed odio sit amet nibh vulputate cursus a sit amet mauris. Morbi accumsan ipsum velit. Nam nec tellus a odio tincidunt auctor a ornare odio. Sed non mauris elit.</p>
        <p>This is Photoshop's version of Lorem Ipsum. Proin gravida nibh vel velit auctor aliquet. Aenean sollicitudin, lorem quis bibendum auctor, nisi elit consequat ipsum, nec sagittis sem nibh id elit. Duis sed odio sit amet nibh vulputate cursus a sit amet mauris.</p>
        <p>This is Photoshop's version of Lorem Ipsum. Proin gravida nibh vel velit auctor aliquet. Aenean sollicitudin, lorem quis bibendum auctor, nisi elit consequat ipsum.</p>
      </div>
      <div class="closing">
        <span class="closing-word">Regard</span>
        <span class="signature">Evan Marlow</span>
      </div>
    </section>
  </main>
</body>
</html>
```